Shop Window Desgin

I have a big glass window (office), 280cm wide by 302cm high and I want designing an advert for our property management business.

Our main colours are in the proeprty management logo attached. I have also uploaded a photo of the shop front (left window), please take into consideration the door.

I want the following text items placed:

PROPERTY MANAGEMENT
HOLIDAY RENTALS
KEYHOLDING
MARKETING & RESERVATIONS
GARDEN & POOL MAINTENACE
CLEANING & LAUNDRY

```html
<!DOCTYPE html>
<html lang="en">
<head>
<meta charset="utf-8">
<title>Harbourline Property Care – Shop Window</title>
<link href="https://fonts.googleapis.com/css2?family=Montserrat:wght@600;800&display=swap" rel="stylesheet">
<style>
  :root {
    --orange: #e8812a;
    --orange-tint: #f4c49a;
    --grey: #6e6e6e;
    --grey-dark: #4a4a4a;
    --grey-pale: #f1f1f1;
    --white: #ffffff;
    --badge-blue: #2a9ad6;
    --backdrop: #e9e6e1;
  }
  * { box-sizing: border-box; margin: 0; padding: 0; }
  html, body { width: 1200px; height: 2480px; overflow: hidden; }
  body {
    background: var(--backdrop);
    font-family: "Montserrat", Arial, sans-serif;
    position: relative;
  }
  .window-sign {
    position: absolute;
    left: 50px; top: 646px;
    width: 1100px; height: 1188px;
    background: linear-gradient(135deg, var(--white) 0%, var(--grey-pale) 100%);
    overflow: hidden;
  }
  .sign-shapes { position: absolute; inset: 0; }
  .brand-mark {
    position: absolute;
    left: 372px; top: 96px;
    width: 108px; height: 108px;
    border-radius: 50%;
    background: var(--orange);
  }
  .brand-name {
    position: absolute;
    left: 512px; top: 86px;
    color: var(--orange);
    font-weight: 800;
    line-height: 1;
    text-transform: uppercase;
  }
  .brand-name .line-main { display: block; font-size: 70px; letter-spacing: -1px; }
  .brand-name .line-sub { display: block; font-size: 38px; margin-top: 10px; }
  .service-list { position: absolute; left: 82px; top: 0; list-style: none; }
  .service {
    position: absolute;
    left: 0;
    display: flex; align-items: center;
    width: 600px;
    transform: translateY(-50%);
  }
  .service-icon {
    width: 84px; height: 84px; flex: none;
    border-radius: 50%;
    background: radial-gradient(circle at 35% 30%, var(--white) 55%, #dcdcdc 100%);
    box-shadow: -8px 6px 10px rgba(0,0,0,0.18);
    display: flex; align-items: center; justify-content: center;
  }
  .service-icon svg { width: 44px; height: 44px; }
  .service-label {
    margin-left: 24px;
    color: var(--white);
    font-weight: 800;
    font-size: 29px;
    line-height: 1.02;
    text-transform: uppercase;
  }
  .web-address {
    position: absolute;
    left: 84px; top: 1114px;
    width: 354px; height: 38px;
    border-radius: 19px;
    background: var(--grey-dark);
    color: var(--white);
    font-weight: 600;
    font-size: 21px;
    display: flex; align-items: center; justify-content: center;
  }
  .partner-badge-round {
    position: absolute;
    left: 758px; top: 1084px;
    width: 86px; height: 66px;
    border-radius: 50%;
    background: var(--badge-blue);
  }
  .partner-badge-bar {
    position: absolute;
    left: 872px; top: 1098px;
    width: 182px; height: 40px;
    border-radius: 6px;
    background: var(--grey);
  }
</style>
</head>
<body>
  <main class="window-sign">
    <svg class="sign-shapes" viewBox="0 0 1100 1188" width="1100" height="1188">
      <defs>
        <linearGradient id="decorGradient" x1="0" y1="1" x2="1" y2="0">
          <stop offset="0" stop-color="#f4c49a"/>
          <stop offset="0.5" stop-color="#e8812a"/>
          <stop offset="1" stop-color="#8a8a8a"/>
        </linearGradient>
      </defs>
      <polygon class="orange-field" points="0,0 84,0 882,936 672,1188 0,1188" fill="#e8812a"/>
      <rect class="brand-decoration" role="img" aria-label="Large brand decoration area"
            x="540" y="420" width="440" height="440" rx="90"
            transform="rotate(45 760 640)" fill="url(#decorGradient)" opacity="0.85"/>
      <rect class="door-guide" x="686" y="452" width="402" height="724" fill="none" stroke="#7a7a7a" stroke-width="1.5"/>
      <rect class="door-guide-inner" x="700" y="466" width="388" height="710" fill="none" stroke="#7a7a7a" stroke-width="1"/>
    </svg>

    <div class="brand-mark"></div>
    <h1 class="brand-name">
      <span class="line-main">Harbourline</span>
      <span class="line-sub">Property Care</span>
    </h1>

    <ul class="service-list">
      <li class="service" style="top:400px">
        <span class="service-icon"><svg viewBox="0 0 24 24" fill="none" stroke="#6e6e6e" stroke-width="1.4"><rect x="7" y="3" width="10" height="14"/><path d="M9 6h2M13 6h2M9 9h2M13 9h2M9 12h2M13 12h2M3 20c3-2 6-2 9 0s6 1 9-1"/></svg></span>
        <span class="service-label">Property<br>Management</span>
      </li>
      <li class="service" style="top:524px">
        <span class="service-icon"><svg viewBox="0 0 24 24" fill="none" stroke="#6e6e6e" stroke-width="1.4"><path d="M3 11l9-7 9 7M5 10v10h14V10"/><rect x="10" y="14" width="4" height="6"/></svg></span>
        <span class="service-label">Holiday<br>Rentals</span>
      </li>
      <li class="service" style="top:654px">
        <span class="service-icon"><svg viewBox="0 0 24 24" fill="none" stroke="#6e6e6e" stroke-width="1.4"><circle cx="9" cy="6" r="3"/><path d="M9 9v7M9 13h3M9 16h2M3 20c3-2 6-2 9 0s6 1 9-1"/></svg></span>
        <span class="service-label">Keyholding</span>
      </li>
      <li class="service" style="top:780px">
        <span class="service-icon"><svg viewBox="0 0 24 24" fill="none" stroke="#6e6e6e" stroke-width="1.4"><path d="M3 10h4l8-4v12l-8-4H3zM6 14l1 5h2M18 9c1 1 1 5 0 6M20 7c2 2 2 8 0 10"/></svg></span>
        <span class="service-label">Marketing &amp;<br>Reservations</span>
      </li>
      <li class="service" style="top:908px">
        <span class="service-icon"><svg viewBox="0 0 24 24" fill="none" stroke="#6e6e6e" stroke-width="1.4"><rect x="4" y="4" width="16" height="16" rx="1"/><path d="M6 9c2-1 4 1 6 0s4-1 6 0M6 13c2-1 4 1 6 0s4-1 6 0M6 17c2-1 4 1 6 0s4-1 6 0"/></svg></span>
        <span class="service-label">Garden &amp;<br>Pool Maintenace</span>
      </li>
      <li class="service" style="top:1034px">
        <span class="service-icon"><svg viewBox="0 0 24 24" fill="none" stroke="#6e6e6e" stroke-width="1.4"><path d="M5 10h10l-1 9H6zM7 10V7h6v3M18 4v12M16 16h4l1 4h-6z"/></svg></span>
        <span class="service-label">Cleaning &amp;<br>Laundry</span>
      </li>
    </ul>

    <div class="web-address">www.harbourlineproperty.com</div>

    <div class="partner-badge-round"></div>
    <div class="partner-badge-bar"></div>
  </main>
</body>
</html>
```